Webdesign für Seminaranbieter
Zielgruppe
Die Velkor Academy bietet Kurse, Seminare & Coachings im Bereich der Kommunikation / Persönlichkeitsentwicklung an.
Folgendes Angebot besteht zur Zeit:
Seminare:
- 'Erste Schritte Dialog', eine Einführung in die Kommunikation.
- 'Sonnige Tage, ruhige Abende' zum Thema Erziehung.
- 'Zeitenwende im Herbst', zum Thema Älter werden und den Umgang damit.
Kurse:
- 'Gewaltfreie Kommunikation', Übungsgruppe
Coaching:
- Einzelsitzungen mit Hypnose
Ps: im Anhang unter 'Angabot_Vorlage.pdf' finden Sie mehr Infos zu den einezlenen Angebote.
Aufgabenstellung
Bitte berücksichtigen Sie, dass bereits ein Logo besteht (siehe Anhang).
Vom gesamteindruck her sollte die Website aufgeräumt, übersichtlich, harmonisch, freundlich & frisch wirken.
Es wäre super, wenn die Website authentisch wirkt (und weniger '0815 Business Website').
Bitte bedenken Sie, dass die Website sich an Private richtet, die sich nach einem 'strahlenderen & unbeschwerterem Lebene sehnen'.
Wir haben bereits viele Persönlichkeiten stärken können und möchten dies auch witerhin mit viel Herzblut machen.

```html
<!DOCTYPE html>
<html lang="de">
<head>
<meta charset="utf-8">
<title>Velkor Academy – Angebote</title>
<link rel="stylesheet" href="https://fonts.googleapis.com/css2?family=Raleway:ital,wght@0,400;0,500;0,600;0,700;1,400&family=Montserrat:wght@400;500;600&display=swap">
<style>
:root{
  --canvas:#efe8e3;
  --white:#ffffff;
  --panel:#f3efea;
  --band:#f0bc8a;
  --accent:#f5734a;
  --label:#d9823f;
  --heading:#5e5169;
  --text:#5b5752;
  --footer:#9c8a78;
  --line:#b9b3ad;
}
*{box-sizing:border-box;margin:0;padding:0}
html,body{width:1200px;height:3562px;overflow:hidden}
body{background:var(--canvas);font-family:"Raleway",sans-serif;color:var(--text);position:relative}
.page{position:absolute;left:135px;top:79px;width:938px}
.abs{position:absolute}

/* hero */
.hero{position:absolute;left:0;top:0;width:938px;height:547px;
  background:radial-gradient(ellipse 55% 45% at 50% 88%,#f0b56a 0%,#c98a74 25%,rgba(90,70,120,0) 70%),
  radial-gradient(ellipse 60% 50% at 55% 30%,#7b6a9a 0%,rgba(40,45,90,0) 70%),
  linear-gradient(180deg,#1e2a4f 0%,#2c3563 45%,#4a4466 75%,#2a2d3c 100%)}
.topbar{position:absolute;left:0;top:0;width:938px;height:55px;background:linear-gradient(180deg,#c9ced9,#aeb7c9)}
.brand-small{position:absolute;left:28px;top:18px;font-family:"Montserrat",sans-serif;font-size:11px;font-weight:500;letter-spacing:1.5px;color:#3b3740}
.nav{position:absolute;top:20px;left:0;width:938px;font-family:"Montserrat",sans-serif;font-size:9.5px;letter-spacing:.5px;color:#3b3740}
.nav span{position:absolute;top:0;white-space:nowrap}
.nav .active{color:var(--accent);border:1px solid var(--accent);padding:3px 10px;top:-4px}
.hero-title{position:absolute;top:335px;width:938px;text-align:center;font-family:"Montserrat",sans-serif;font-weight:400;font-size:39px;letter-spacing:6px;color:#fff}
.hero-tag{position:absolute;top:394px;width:938px;text-align:center;font-family:"Montserrat",sans-serif;font-size:18px;letter-spacing:2px;color:#fff}
.dots{position:absolute;top:523px;left:452px;display:flex;gap:6px}
.dots i{width:7px;height:7px;border:1px solid #fff;border-radius:50%;display:block}
.dots i.on{background:#fff}

/* newsletter */
.newsletter{position:absolute;left:0;top:564px;width:938px;height:61px;background:var(--band)}
.newsletter .txt{position:absolute;left:136px;top:14px;font-family:"Montserrat",sans-serif;color:#fff;font-size:11px;line-height:16px;letter-spacing:.8px}
.newsletter .txt b{font-weight:500;letter-spacing:1.5px}
.field{position:absolute;background:#fff;border:1px solid var(--line);font-family:"Montserrat",sans-serif;font-size:9.5px;letter-spacing:1px;color:#8f8a85;padding-left:11px}
.newsletter .field{left:407px;top:16px;width:329px;height:30px;line-height:28px;border-color:#fff}
.ok{position:absolute;left:750px;top:19px;width:40px;height:24px;background:var(--accent);color:#fff;font-size:10px;font-family:"Montserrat",sans-serif;text-align:center;line-height:24px}

/* offers */
.intro{position:absolute;left:0;top:625px;width:938px;height:149px;background:var(--white)}
.intro h1{position:absolute;top:76px;width:938px;text-align:center;font-family:"Montserrat",sans-serif;font-weight:500;font-size:26px;letter-spacing:1.2px;color:var(--heading)}
.seminar{position:absolute;left:0;width:938px;background:var(--panel)}
.gap{position:absolute;left:0;width:938px;background:var(--white)}
.photo{position:absolute}
.seminar h2{position:absolute;left:377px;font-family:"Montserrat",sans-serif;font-weight:600;font-size:16px;color:var(--heading);white-space:nowrap}
.facts{position:absolute;left:377px;width:540px;font-family:"Montserrat",sans-serif;font-size:12.5px;font-weight:600;color:var(--label)}
.facts div{height:32px;position:relative;white-space:nowrap}
.facts span:last-child{position:absolute;left:81px;top:0;white-space:nowrap}
.btn{position:absolute;width:126px;height:31px;background:var(--accent);color:#fff;font-family:"Montserrat",sans-serif;font-size:11px;letter-spacing:1.2px;text-align:center;line-height:31px}
.copy{position:absolute;left:49px;width:796px;font-size:10.8px;line-height:15px}
.copy p+p{margin-top:12px}
.agenda-title{position:absolute;left:49px;font-family:"Montserrat",sans-serif;font-size:15.5px;font-weight:500;letter-spacing:.5px;color:var(--heading)}
.agenda-row{position:absolute;left:49px;width:840px;font-size:11px;line-height:15px}
.agenda-row .lbl{position:absolute;left:0;top:0;font-family:"Montserrat",sans-serif;font-weight:600;font-size:12px;color:var(--label);white-space:nowrap}
.agenda-row .body{position:absolute;top:0;white-space:nowrap}

/* landscape & contact */
.landscape{position:absolute;left:-2px;top:2716px;width:940px;height:260px;
  background:radial-gradient(ellipse 40% 60% at 75% 20%,#f4efe6 0%,rgba(244,239,230,0) 70%),
  linear-gradient(180deg,#d8d2ca 0%,#c2b8ae 50%,#5c5550 80%,#2f2b29 100%)}
.contact{position:absolute;left:0;top:2976px;width:938px;height:350px;background:var(--white)}
.contact .brand{position:absolute;left:0;width:392px;text-align:center;font-family:"Montserrat",sans-serif;color:#2f2c30}
.contact .brand-name{top:114px;font-size:17px;letter-spacing:3px}
.contact .addr{top:171px;font-size:12.5px;line-height:17px;letter-spacing:.5px;color:#4b4744}
.contact .addr b{font-weight:600;letter-spacing:1px}
.contact h3{position:absolute;left:489px;top:30px;font-family:"Montserrat",sans-serif;font-weight:400;font-size:12.5px;line-height:16px;letter-spacing:1px;color:#3b3740}
.contact .field{left:489px;width:329px}
.footer{position:absolute;left:-2px;top:3326px;width:940px;height:79px;background:var(--footer);color:#fff;font-family:"Montserrat",sans-serif;font-size:12.5px;letter-spacing:1px}
.footer span{position:absolute;top:33px}
</style>
</head>
<body>
<div class="page">

  <div class="hero" role="img" aria-label="Nachthimmel mit Milchstraße, Silhouetten einer Gruppe mit erhobenen Armen am Horizont">
    <div class="topbar"></div>
    <div class="brand-small">VELKOR ACADEMY</div>
    <nav class="nav">
      <span style="left:657px">HOME</span>
      <span class="active" style="left:708px">ANGEBOT</span>
      <span style="left:784px">KONTAKT</span>
      <span style="left:849px">ÜBER UNS</span>
    </nav>
    <svg class="abs" style="left:22px;top:262px" width="22" height="38" viewBox="0 0 22 38"><path d="M20 2 L3 19 L20 36" fill="none" stroke="#fff" stroke-width="2"/></svg>
    <svg class="abs" style="left:895px;top:262px" width="22" height="38" viewBox="0 0 22 38"><path d="M2 2 L19 19 L2 36" fill="none" stroke="#fff" stroke-width="2"/></svg>
    <div class="hero-title">VELKOR ACADEMY</div>
    <div class="hero-tag">NEUE PERSPECTIVEN · NEUE HORIZONTE</div>
    <div class="dots"><i></i><i class="on"></i><i></i></div>
  </div>

  <div class="newsletter">
    <div class="txt"><b>KOSTENLOSES ERSTGESPRÄCH</b><br>Abonnieren Sie unseren Newsletter!</div>
    <div class="field">E-MAIL ADRESSE</div>
    <div class="ok">OK</div>
  </div>

  <section class="intro"><h1>UNSERE AKTUELLE ANGEBOTE</h1></section>

  <section class="seminar" style="top:774px;height:907px">
    <div class="photo" role="img" aria-label="Sepiafoto einer Familie, die Hand in Hand über eine Brücke läuft" style="left:49px;top:44px;width:271px;height:248px;background:linear-gradient(160deg,#d9d2c6,#a79c8c 60%,#8a8073)"></div>
    <h2 style="top:45px">SEMINAR: Sonnige Tage, ruhige Abende</h2>
    <div class="facts" style="top:86px">
      <div><span>ZIEL</span><span>Entspanntes und erfülltes Leben mit Kinder</span></div>
      <div><span>DAUER</span><span>4 Abende à 1.5 Stunden</span></div>
      <div><span>KOSTEN</span><span>CHF 280.-</span></div>
      <div><span>ORT</span><span>Basel, Lindenhof</span></div>
      <div><span>DATUM</span><span>7-11. Mai 2019.</span></div>
    </div>
    <div class="btn" style="left:377px;top:261px">ANMELDEN</div>
    <div class="copy" style="top:339px">
      <p><i>„Unter Erziehung versteht man die pädagogische Einflussnahme auf die Entwicklung und das Verhalten Heranwachsender“.</i> Erziehungstheorien gibt es unzählige, die das Spektrum von streng und autoritär bis hin zum Laisser-faire decken. Das selbst erlebte wird z.T. auch unreflektiert wiederholt und/oder wir verlieren uns in unzählige Ratgeber.</p>
      <p>Mithilfe der Neurowissenschaften wird uns klar, dass das oft kräftezerrende Ringen rund um die Erziehung absolut unnötig und überflüssig ist, ja sogar schädigend. Am wirksamsten und effektivsten begleiten wir die Entwicklung eines Kindes mit Beziehung und Selbst-Erziehung – das ist die magische Formel. Indem wir zu nachahmenswerten Erwachsenen werden, fördern wir unsere eigene Persönlichkeitsentwicklung und ermöglichen damit eine harmonische, authentische und unterstützende Umgebung für die Kinder. Im 2. Teil gehen wir der Frage nach, wie Eltern ihre Kindern verhelfen zu starken, selbstsicheren und erfüllten Erwachsenen zu werden, die ihren eigenen Platz in der Gesellschaft kreieren – jenseits von Konkurrenzkampf und Studiumsinflation.</p>
    </div>
    <div class="agenda-title" style="top:541px">AGENDA</div>
    <div class="agenda-row" style="top:580px"><span class="lbl">1. ABEND</span><div class="body" style="left:87px">• Lorem ipsum dolor sit amet<br>• In wisi facilisis vel, cum ut praesent dignissim<br>• Quem explicari ne mei. An mei mazim facilisis, vel ut munere postea putent, cu nulla melius omittam eum.</div></div>
    <div class="agenda-row" style="top:641px"><span class="lbl">2. ABEND</span><div class="body" style="left:89px">• Lorem ipsum dolor sit amet<br>• In wisi facilisis vel, cum ut praesent dignissim<br>• Quem explicari ne mei.<br>• An mei mazim facilisis, vel ut munere postea putent, cu nulla melius omittam eum.</div></div>
    <div class="agenda-row" style="top:717px"><span class="lbl">3. ABEND</span><div class="body" style="left:87px">• In wisi facilisis vel, cum ut praesent dignissim<br>• Quem explicari ne mei.<br>• Putent, cu nulla melius omittam eum</div></div>
    <div class="agenda-row" style="top:779px"><span class="lbl">4. ABEND</span><div class="body" style="left:87px">• Lorem ipsum dolor sit amet<br>• In wisi facilisis vel, cum ut praesent dignissim<br>• Quem explicari ne mei. An mei mazim facilisis, vel ut munere postea putent, cu nulla melius omittam eum.</div></div>
    <div class="btn" style="left:403px;top:854px">ANMELDEN</div>
  </section>

  <div class="gap" style="top:1681px;height:37px"></div>

  <section class="seminar" style="top:1718px;height:947px">
    <div class="photo" role="img" aria-label="Nahaufnahme eines Uhrenzifferblatts mit Zeigern" style="left:52px;top:50px;width:283px;height:246px;background:linear-gradient(135deg,#4a4744,#9a9590 45%,#e2ded8 70%,#8c8782)"></div>
    <h2 style="top:52px">SEMINAR: Zeit und Alternativen</h2>
    <div class="facts" style="top:93px">
      <div><span>ZIEL</span><span>„Mehr leben in Deine Jahre und mehr Jahre in Deinem Leben“</span></div>
      <div><span>DAUER</span><span>1 Tag</span></div>
      <div><span>KOSTEN</span><span>CHF 280.-</span></div>
      <div><span>ORT</span><span>Schloss Auenhof</span></div>
      <div><span>DATUM</span><span>11. Mai 2019.</span></div>
    </div>
    <div class="btn" style="left:378px;top:260px">ANMELDEN</div>
    <div class="copy" style="top:342px">
      <p>Zeit ist ein allgegenwärtiges (und manchmal leidiges) Thema, wie z.B „keine Zeit haben“ oder „die Zeit verfliegt im Nu“. Was IST jedoch Zeit? Wie und wo nehmen wir sie wahr? Welche Auswirkungen hat das „Zeit denken“? Was wäre, wenn wir der Zeit entkommen – aussteigen – könnten? Mit welchen Folgen? Welchen Zusammenhang haben Zeit und Alter?</p>
      <p>Wir setzen uns mit unseren Vorstellungen vom Alter auseinander und stellen dem bahnbrechende Entdeckungen der Neurowissenschaften gegenüber. Aus der passiven Erwartungshaltung steigen wir in ein aktiv gewähltes altern.</p>
      <p><i>„Älter werden ist unumgänglich. Alt werden ist optional.“</i></p>
    </div>
    <div class="agenda-title" style="top:504px">AGENDA</div>
    <div class="agenda-row" style="top:543px"><span class="lbl">1. BLOCK</span><div class="body" style="left:121px">08:00 - 10:00<br>Was ist Zeit? Die Erfindung der Zeit<br>Wie hat dieser begriff unser Bewusstsein geprägt, mit welchen Folgen?</div></div>
    <div class="agenda-row" style="top:606px"><span class="lbl">2. BLOCK</span><div class="body" style="left:122px">10:00-12:00<br>Wo finden wir aus der Zeit heraus? Wo gibt es keine Zeit?<br>Praktische Übung_ Achtsamkeit</div></div>
    <div class="agenda-row" style="top:667px"><span class="lbl">MITTAGSPAUSE</span><div class="body" style="left:122px">12:00 - 13:30</div></div>
    <div class="agenda-row" style="top:720px;left:47px"><span class="lbl">3. BLOCK</span><div class="body" style="left:121px">13:30 - 15:30<br>Bezug von Zeit und Alter – unsere Vorstellungen wahrnehmen:<br>Ist altern ein naturgegebener Prozess dem wir unterworfen sind oder können wir es steuern? Wir gehen der Frage nach,<br>wie eine differenzierte und bewusst gewählte Auffassung von Zeit und älter werden sich auswirken.</div></div>
    <div class="agenda-row" style="top:791px;left:47px"><span class="lbl">4. BLOCK</span><div class="body" style="left:121px">15:30 - 17:00<br>Bahnbrechende Aussichten.<br>Fazit: Für welches altern entscheiden wir uns?<br>Dankbarkeit und Fülle</div></div>
    <div class="btn" style="left:403px;top:886px">ANMELDEN</div>
  </section>

  <div class="gap" style="top:2665px;height:51px"></div>

  <div class="landscape" role="img" aria-label="Person sitzt bei Sonnenaufgang auf einem Felsvorsprung über einem nebligen Tal"></div>

  <section class="contact">
    <div class="brand brand-name">VELKOR ACADEMY</div>
    <div class="brand addr"><b>VELKOR ACADEMY GMBH.</b><br><br>Lindenweg 17<br>4321 Beispielheim<br><br>TEL: 0176 555 208<br>info@velkoracademy.ch</div>
    <h3>NOCH FRAGEN, ANREGUNGEN?<br>SCHREIBEN SIE UNS!</h3>
    <div class="field" style="top:79px;height:31px;line-height:29px">NAME</div>
    <div class="field" style="top:125px;height:30px;line-height:28px">E-MAIL ADRESSE</div>
    <div class="field" style="top:166px;height:101px;line-height:28px">NACHRICHT</div>
    <div class="btn" style="left:489px;top:282px;width:163px;height:35px;line-height:35px">SENDEN</div>
  </section>

  <footer class="footer">
    <span style="left:58px">Datenschutz</span>
    <span style="left:178px">Impressum</span>
    <span style="left:399px">VELKOR ACADEMY | 2019</span>
  </footer>

</div>
</body>
</html>
```